Velvet nook need a simple quirky modern straight to the point brochure of our group, our project and

I need a 5-10-page website that captures the ethos and the identity of Velvet Nook which is a brand-new project and concept providing first class professional locations and facilities to perform in carefully chosen categories working on several existing platforms in teams enjoying the flexibility in our approach.
This is a project that has been planned for 3 years.
The adult webcam industry is growing annually and rapidly and its split into two main sections. The first section is the Independent Models that are usually found to be working in more developed and fortunate countries such as the UK, Canada, USA and Western Europe. These independent models work on the same platforms as everyone else but are working from their homes alone in a designated room at a convenient time and on their own personal accounts. This section is growing rapidly now especially in the UK as women are learning that this is a very good way to make extra money in a safe and professional manner on established websites across the world and it’s this word of mouth progression that has caused the recent flood of potential models appearing on the sites. Although this section is growing rapidly the percentage of models who are what we class as successful considerably lower than that of the other side of the industry.

This side of the industry are the webcam studios. A studio is a place where a model can work in her own allocated room amongst other models who work in their own room where the IT equipment and professional lighting is provided. These models tend to be more serious about the role of a webcam model and treat it as a proper job putting the right number of hours in making more effort on how they present themselves and, in most cases, using several platforms when they broadcast at any one time. It’s a proven fact that in general the theme seems to show women working in professional studios are more successful than that of the independent models even though they usually give 50% of their earning to the studio as a rental payment. These places/premises are usually found in less developed countries where money and opportunities to earn it are far greater. These nations include Romania (the capital of webcam world with over 2000 active studios operating at any one time) Others to mention are Russia, Columbia, China, Philippines, Latvia, and other Eastern European Countries.
The models are not in our view treat with the flexibility they deserve, and we feel the conditions that are imposed are generally designed to suit the studio not the model.

In the UK there are several large established "groups" that have a lot of models signed to their group, but the models work independently from home. We know through our research these models get the same split (50%) as the studio models we also know a lot about but work alone with no real training or support. These groups are mainly based in the United Kingdom and USA and the numbers of the models joining them is growing at a ridiculous rate. The models also tend to be what we feel treat as another bum on a seat and the business plan seems to be the more models that sign the more the group account make.

Velvet Nook is completely different. We want to set up designated Studios that are accessible to all our models where we can professionally train support and advise new models and offer them the freedom and flexibility to work in our professional operated studios and their own homes which brings both sides of the industry together into one.

Velvet Nook is a group and idea that has formed from what can only be described as a spiritual special journey. Perfect foundations we feel to build something unique and magical.

We are a small team at the moment that come from different cultures, countries with diverse and valuable life experiences. Combined in unity our experiences skills and knowledge are better shared as we now work closely together preparing the start of this exciting new project. We have formed into what we believe is a very strong team over a very natural unplanned three-year period and together we share the same ethos, positive energies and vision as we move forward towards achieving our goals and our dream.

Our goal is to create very special groups of different types of people similar to ourselves who we believe will help us provide a very welcome refreshing change to how video chat is currently offered, performed, directed and received in the UK and beyond.

To achieve our goals, we believe we should start by creating special places where we can professionally introduce the industry, the right things to know and to do, the ins and the outs, answering all your questions properly whilst offering our honest opinions and advice.
We want these places to provide the unique rewards, the most creative, original and exciting incentives. Places where there is always quality home cooked food provided. Places that look after the responsibilities of buying expensive outfits and costumes or shoes or boots. Places that understand that make up and cosmetics are expensive and help buy the things that our models need.
We don’t want these places to imply strict rules and silly policies or even have people who think they are in charge but offer no benefit to themselves never mind the team. A place that shows you the easiest way to do this having the most fun and laughing the hardest.
Places that we know where everyone will make special and even much needed friends. We are now ready to set up our first studio premises which will offer the very best carefully and professionally thought out introductions for anybody who would like to see for themselves just how interesting, opportunistic, fun and rewarding the wonderful world of webcamming/video chat is and will continue to be for some time to come.
Believe us when we say anybody can do this, have fun and be successful.
The first webcam studio is based in Sheffield, South Yorkshire, England and is first instalment of what will become successful Harbour Circle franchise and original Adult brand that dares to break the rules to make a positive difference for everyone

The Studio is going to be called Velvet Nook and the slogan we have adopted which is important is "your secret sanctuary" which hits the nail on the head considering what we are opening our project from a location point of view. We will be using houses or residential properties initially and converting them into purpose build training studios with carefully thought out room designing with themes and classy vintage boutique styling. We will be focusing on more classy outfits for the models to wear which will be provided and all the areas of the studio will have quirky touches - (ideas - jukebox, stylising areas, home cooked cuisine available for the girls to eat, wine and other refreshments, chill out areas, potentially a child free zone. gym equipment and maybe a solarium to give you a better idea)
The focus and theme around the branding is teamwork, helping, caring, encouraging, incentivising and having fun making very good money in healthy environments - basically using my experience from being a sales director for a small then large IT company for 12 years (where I broke all the corporate rules to achieve the same ethos above)
Main message is probably flexibility, care and respect and the fact that this job is not exactly how a person who imagines it sees it exactly for what it is. We are thinking out of the box and putting all the good things ideas and experiences together and taking all the bad things, we have seen and experienced out of the mix. We all must create a place where the models would all agree and promote the slogans message - "your secret sanctuary"
perfect for single mums, students, people who need to earn more money that their main income, curious ladies or ladies who have lost their personal confidence for whatever reason (usually a man’s fault) also perfect for people who love working in teams.
I want the website to be a classy straight to the point brochure of our brand and ethos to create an image that can grow as we move forward. It MUST provide the following ...
1 - Flexibility to be changed easily by me or my team
2 - We have signed up to a corporate business portal on www.hostquill.co.uk which is a business portal, and, in that subscription, we have paid for a domain name (www.velvetnook-cam.com) and we can host our site from their portal. I have no idea how to do this so will need help please.
3 - the ability to receive requests from models and distribute them to assigned mailboxes/email addresses.
4 - IMPORTANT
The ability and option to be upgraded to be able to offer live video streaming directly from our own group and website which eradicates the issue where we must pay between 30 -40% of the money we make to the websites we currently work on and where we are experienced. Examples of the sites we will use are Glimmerhub.com - nightorchid.com and quillstream.com (mainly the first two)
I would love to be able to upgrade the website after we have settled into the project and be able to stream directly from our studios or independent model’s location. This would have to be very simple for the model to use and the customer and I would say night Orchid is the best example of how simple it needs to be. For this to be achieved we would need to have the facility to write profiles for each model, show their status (live etc) and be able to take payments from members to be used as purchase tokens to be redeemed within the site with our models. Something for the future and the ability to partner with a person or team to achieve this target would be ideal and a natural progression.

5 - the ability to play chosen music on certain pages with admin flexibility to change

6 - the ability to play videos that we may design for marketing purposes.

7 - Some sort of tracking device or system that can alert us of anyone who clicks on a certain location providing potential leads for us to follow. (least important)

I have tried to do this myself using the many build your own websites that are available, but I have given up. I want something as perfect as possible projecting our ethos and direction as clearly and quirky as possible.

Side Notes - there are lots of opportunities posted on job groups on Friendlane that when we consider the feedback from people using them seem to be fake or offering people false and unrealistic opportunities. We want to focus on these groups in our marketing campaigns but somehow make the point that we are aware there are lots of let’s say amazing jobs out there on these Friendlane groups that do not always meet people’s expectations in the end. Velvet Nook is real, and we do what we say.
I’m a very spiritual person and also an expert in astrology. I am also interested in numerology. I would like to in a very subtle quirky way include something in the deign related to spirituality, to my number in numerology which is number 11 and to my sign which is Sagittarius. I can help people using my knowledge and skills surrounding these interests and I have a proven track record when working as a director in corporate IT sales.

We have set up a limited business (Dorvex Limited) which will be the company owning any trading name such as Velvet Nook but for the first six months I want to class this a project before officially stating the business details online.

I have the logos designed that I will include. The picture that is a cross with Bruno Halvers is a logo for a clothing designer i love so I sent. Also included are some screenshots from the attempts I made trying to design a website : )
Colours to consider - Grey shades - Pink - white - sage/olive green

Any questions please ask

Thanks
Owen

Target Market(s)

students - single mums any openminded women wanting to work as part of a team via our studio premises or the flexibilty to work from home in sheffield and south yorkshire initially

Coding

Coded - Design and coding required

Number of Pages Required

5+ page

Font styles to use
Sans Serif

Colors

Designer to choose colors to be used in the design.

Requirements
Must have
• It MUST provide the following ...
• 1 - Flexibility to be changed easily by me or my team
• 2 - We have signed up to a corporate business portal on www.hostquill.co.uk which is a business portal, and, in that subscription, we have paid for a domain name (www.velvetnook-cam.com) and we can host our site from their portal. I have no idea how to do this so will need help please.
• 3 - the ability to receive requests from models and distribute them to assigned mailboxes/email addresses.
• 4 - IMPORTANT
• The ability and option to be upgraded to be able to offer live video streaming directly from our own group and website which eradicates the issue where we must pay between 30 -40% of the money we make to the websites we currently work on and where we are experienced. Examples of the sites we will use are Glimmerhub.com - nightorchid.com and quillstream.com (mainly the first two)
• I would love to be able to upgrade the website after we have settled into the project and be able to stream directly from our studios or independent model’s location. This would have to be very simple for the model to use and the customer and I would say night Orchid is the best example of how simple it needs to be. For this to be achieved we would need to have the facility to write profiles for each model, show their status (live etc) and be able to take payments from members to be used as purchase tokens to be redeemed within the site with our models. Something for the future and the ability to partner with a person or team to achieve this target would be ideal and a natural progression.
• 5 - the ability to play chosen music on certain pages with admin flexibility to change
• 6 - the ability to play videos that we may design for marketing purposes.
• 7 - Some sort of tracking device or system that can alert us of anyone who clicks on a certain location providing potential leads for us to follow. (least important)
• A simplke functioning online form where models can apply for opportunities or register their interest.
Nice to have
• All in the project description

```html
<!DOCTYPE html>
<html lang="en">
<head>
<meta charset="utf-8">
<title>Velvet Nook – Your Secret Sanctuary</title>
<link href="https://fonts.googleapis.com/css2?family=Roboto:wght@400;500;700;900&display=swap" rel="stylesheet">
<style>
  :root{
    --page:#101010;
    --header:#0b0b0b;
    --sidebar:#1a1a1a;
    --main:#a3126f;
    --main-deep:#7d0b54;
    --pink:#e0209a;
    --pink-dark:#b3107f;
    --label:#222;
    --muted:#bbb;
    --white:#fff;
    --black:#0a0a0a;
    --shade:rgba(0,0,0,.58);
    --tone-blush:#e6a9b8;
    --tone-rose:#b8577c;
    --tone-plum:#6e2b55;
    --tone-sand:#d8b49a;
    --tone-mauve:#9a6a8c;
    --tone-sage:#8e9a7a;
  }
  *{box-sizing:border-box;margin:0;padding:0}
  html,body{width:843px;height:1200px;overflow:hidden}
  body{background:var(--page);font-family:"Roboto",Arial,sans-serif;color:var(--white);position:relative}

  .site-header{position:absolute;left:0;top:0;width:843px;height:56px;background:var(--header)}
  .brand{position:absolute;left:14px;top:16px;font-size:20px;font-weight:700;color:var(--pink)}
  .search{position:absolute;left:219px;top:16px;width:287px;height:22px;background:var(--white);display:flex}
  .search-field{flex:1;font-size:9px;color:#888;padding:6px 8px}
  .search-btn{width:24px;background:var(--pink);display:flex;align-items:center;justify-content:center}
  .account-links{position:absolute;right:24px;top:12px;font-size:9px;color:var(--muted);display:flex;gap:12px}
  .lang{position:absolute;right:24px;top:32px;width:56px;height:14px;border:1px solid #444;font-size:8px;color:var(--muted);padding:2px 4px}

  .sidebar{position:absolute;left:0;top:56px;width:190px;height:1030px;background:var(--sidebar)}
  .menu{list-style:none;padding:18px 0 0 16px}
  .menu li{font-size:11px;color:var(--muted);height:31px;line-height:31px}

  .main{position:absolute;left:190px;top:56px;width:653px;height:1030px;background:var(--main)}
  .banner{position:absolute;left:8px;top:8px;width:637px;height:214px;background:
      radial-gradient(circle at 88% 30%,#f7c6e0 0 40px,transparent 42px),
      radial-gradient(circle at 78% 62%,#e86ab4 0 34px,transparent 36px),
      linear-gradient(120deg,#c63c93,#e98cc2 58%,#b52d83)}
  .banner-title{position:absolute;left:68px;top:40px;font-size:44px;font-weight:900;color:rgba(255,255,255,.55);letter-spacing:1px}
  .banner-tag{position:absolute;left:70px;top:96px;font-size:14px;font-weight:500;color:rgba(255,255,255,.75);letter-spacing:2px}

  .models{position:absolute;left:10px;top:234px;display:grid;grid-template-columns:repeat(4,148px);column-gap:13px;row-gap:13px}
  .model-card{height:220px}
  .model-photo{height:138px}
  .model-card:nth-child(4n+1) .model-photo{background:linear-gradient(160deg,var(--tone-blush),var(--tone-rose) 60%,var(--tone-plum))}
  .model-card:nth-child(4n+2) .model-photo{background:linear-gradient(200deg,var(--tone-sand),var(--tone-mauve) 65%,#4a2a3e)}
  .model-card:nth-child(4n+3) .model-photo{background:linear-gradient(150deg,#f2d3da,var(--tone-blush) 45%,var(--tone-rose))}
  .model-card:nth-child(4n+4) .model-photo{background:linear-gradient(180deg,var(--tone-mauve),var(--tone-plum) 70%,#3a1830)}
  .model-card:nth-child(5) .model-photo,.model-card:nth-child(10) .model-photo{background:linear-gradient(170deg,#c9b8a4,var(--tone-sage) 55%,#4f5a45)}
  .model-label{height:18px;background:var(--label);display:flex;align-items:center;justify-content:space-between;padding:0 6px;font-size:8px}
  .model-text{font-size:7.5px;line-height:12px;color:#f3c9e3;text-align:center;padding:7px 4px 6px;height:38px}
  .chat-btn{display:block;margin:0 auto;width:66px;height:20px;background:var(--black);font-size:8px;font-weight:700;text-align:center;line-height:20px}

  .pager{position:absolute;left:296px;top:978px;display:flex;gap:4px}
  .pager span{width:16px;height:16px;background:var(--main-deep);font-size:8px;text-align:center;line-height:16px}

  .site-footer{position:absolute;left:0;top:1086px;width:843px;height:114px;background:var(--header);text-align:center}
  .footer-links{font-size:8px;color:var(--muted);padding-top:22px;word-spacing:4px}
  .footer-note{font-size:7px;color:#888;line-height:11px;margin-top:8px}
  .copyright{position:absolute;left:14px;bottom:12px;font-size:7px;color:#777}
  .social{position:absolute;right:24px;bottom:10px;display:flex;gap:6px}
  .social span{width:12px;height:12px;border-radius:50%;background:var(--pink)}

  .overlay{position:absolute;inset:0;background:var(--shade)}

  .age-modal{position:absolute;left:135px;top:155px;width:573px;height:309px;background:var(--white)}
  .age-head{height:174px;background:linear-gradient(135deg,var(--pink),var(--pink-dark));text-align:center}
  .age-big{font-size:38px;font-weight:700;line-height:40px;padding-top:26px}
  .age-sub{font-size:34px;font-weight:700;line-height:40px;margin-top:16px}
  .silhouette{position:absolute;left:24px;top:14px;width:80px;height:226px;border-radius:40px 40px 10px 10px;background:linear-gradient(180deg,rgba(40,0,30,.45),rgba(60,0,40,.3) 68%,rgba(180,180,180,.35))}
  .age-body{text-align:center;color:#222;padding-top:14px}
  .age-copy{font-size:10px;line-height:16px}
  .age-title{font-size:12px;font-weight:700;color:var(--pink);margin-top:6px}
  .age-actions{display:flex;justify-content:center;gap:14px;margin-top:8px}
  .age-btn{height:32px;padding:0 14px;font-size:16px;font-weight:700;color:var(--white);line-height:32px}
  .age-btn.under{background:var(--black)}
  .age-btn.enter{background:var(--pink)}
</style>
</head>
<body>
  <header class="site-header">
    <div class="brand">Velvet Nook</div>
    <div class="search">
      <div class="search-field">Search models…</div>
      <div class="search-btn"><svg width="10" height="10" viewBox="0 0 10 10"><circle cx="4" cy="4" r="3" fill="none" stroke="#fff" stroke-width="1.4"/><line x1="6.2" y1="6.2" x2="9.2" y2="9.2" stroke="#fff" stroke-width="1.4"/></svg></div>
    </div>
    <div class="account-links"><span>Login</span><span>Register</span><span>Help</span></div>
    <div class="lang">English ▾</div>
  </header>

  <nav class="sidebar">
    <ul class="menu">
      <li>Home</li><li>About Us</li><li>Our Studios</li><li>Models</li><li>Live Now</li><li>Work With Us</li><li>Training</li><li>Apply</li><li>FAQ</li><li>Blog</li><li>Contact</li><li>Login</li><li>Sign Up</li>
    </ul>
  </nav>

  <main class="main">
    <div class="banner" role="img" aria-label="Studio banner photo with pink balloons">
      <div class="banner-title">VELVET NOOK</div>
      <div class="banner-tag">YOUR SECRET SANCTUARY</div>
    </div>

    <section class="models">
      <article class="model-card"><div class="model-photo" role="img" aria-label="Model profile photo"></div><div class="model-label"><span>Ruby Rose</span><svg width="8" height="8" viewBox="0 0 10 9"><path d="M5 9 1 5a2.4 2.4 0 0 1 4-3 2.4 2.4 0 0 1 4 3z" fill="#fff"/></svg></div><p class="model-text">Trained at our Sheffield<br>studio, come say hello</p><span class="chat-btn">LIVE CHAT</span></article>
      <article class="model-card"><div class="model-photo" role="img" aria-label="Model profile photo"></div><div class="model-label"><span>Sienna Belle</span><svg width="8" height="8" viewBox="0 0 10 9"><path d="M5 9 1 5a2.4 2.4 0 0 1 4-3 2.4 2.4 0 0 1 4 3z" fill="#fff"/></svg></div><p class="model-text">Live from my vintage<br>boutique room tonight</p><span class="chat-btn">LIVE CHAT</span></article>
      <article class="model-card"><div class="model-photo" role="img" aria-label="Model profile photo"></div><div class="model-label"><span>Lola Grey</span><svg width="8" height="8" viewBox="0 0 10 9"><path d="M5 9 1 5a2.4 2.4 0 0 1 4-3 2.4 2.4 0 0 1 4 3z" fill="#fff"/></svg></div><p class="model-text">Student by day, team<br>player by night</p><span class="chat-btn">LIVE CHAT</span></article>
      <article class="model-card"><div class="model-photo" role="img" aria-label="Model profile photo"></div><div class="model-label"><span>Mia Vale</span><svg width="8" height="8" viewBox="0 0 10 9"><path d="M5 9 1 5a2.4 2.4 0 0 1 4-3 2.4 2.4 0 0 1 4 3z" fill="#fff"/></svg></div><p class="model-text">Chatty and cheeky<br>see you soon</p><span class="chat-btn">LIVE CHAT</span></article>
      <article class="model-card"><div class="model-photo" role="img" aria-label="Model profile photo"></div><div class="model-label"><span>Ava Lune</span><svg width="8" height="8" viewBox="0 0 10 9"><path d="M5 9 1 5a2.4 2.4 0 0 1 4-3 2.4 2.4 0 0 1 4 3z" fill="#fff"/></svg></div><p class="model-text">Working from home with<br>the Velvet Nook team</p><span class="chat-btn">LIVE CHAT</span></article>
      <article class="model-card"><div class="model-photo" role="img" aria-label="Model profile photo"></div><div class="model-label"><span>Nina Star</span><svg width="8" height="8" viewBox="0 0 10 9"><path d="M5 9 1 5a2.4 2.4 0 0 1 4-3 2.4 2.4 0 0 1 4 3z" fill="#fff"/></svg></div><p class="model-text">Jukebox on, music and<br>lovely talks</p><span class="chat-btn">LIVE CHAT</span></article>
      <article class="model-card"><div class="model-photo" role="img" aria-label="Model profile photo"></div><div class="model-label"><span>Cleo Fox</span><svg width="8" height="8" viewBox="0 0 10 9"><path d="M5 9 1 5a2.4 2.4 0 0 1 4-3 2.4 2.4 0 0 1 4 3z" fill="#fff"/></svg></div><p class="model-text">Studio girl with<br>big smiles</p><span class="chat-btn">LIVE CHAT</span></article>
      <article class="model-card"><div class="model-photo" role="img" aria-label="Model profile photo"></div><div class="model-label"><span>Ella Moss</span><svg width="8" height="8" viewBox="0 0 10 9"><path d="M5 9 1 5a2.4 2.4 0 0 1 4-3 2.4 2.4 0 0 1 4 3z" fill="#fff"/></svg></div><p class="model-text">New in, supported and<br>full of fun</p><span class="chat-btn">LIVE CHAT</span></article>
      <article class="model-card"><div class="model-photo" role="img" aria-label="Model profile photo"></div><div class="model-label"><span>Tia Sage</span><svg width="8" height="8" viewBox="0 0 10 9"><path d="M5 9 1 5a2.4 2.4 0 0 1 4-3 2.4 2.4 0 0 1 4 3z" fill="#fff"/></svg></div><p class="model-text">Yorkshire charm<br>every night</p><span class="chat-btn">LIVE CHAT</span></article>
      <article class="model-card"><div class="model-photo" role="img" aria-label="Model profile photo"></div><div class="model-label"><span>Jade Wren</span><svg width="8" height="8" viewBox="0 0 10 9"><path d="M5 9 1 5a2.4 2.4 0 0 1 4-3 2.4 2.4 0 0 1 4 3z" fill="#fff"/></svg></div><p class="model-text">Classy, calm and<br>always kind</p><span class="chat-btn">LIVE CHAT</span></article>
      <article class="model-card"><div class="model-photo" role="img" aria-label="Model profile photo"></div><div class="model-label"><span>Zara Bloom</span><svg width="8" height="8" viewBox="0 0 10 9"><path d="M5 9 1 5a2.4 2.4 0 0 1 4-3 2.4 2.4 0 0 1 4 3z" fill="#fff"/></svg></div><p class="model-text">Single mum, flexible<br>hours, good stories</p><span class="chat-btn">LIVE CHAT</span></article>
      <article class="model-card"><div class="model-photo" role="img" aria-label="Model profile photo"></div><div class="model-label"><span>Lily Dawn</span><svg width="8" height="8" viewBox="0 0 10 9"><path d="M5 9 1 5a2.4 2.4 0 0 1 4-3 2.4 2.4 0 0 1 4 3z" fill="#fff"/></svg></div><p class="model-text">Online most nights<br>say hi</p><span class="chat-btn">LIVE CHAT</span></article>
    </section>

    <div class="pager"><span>‹</span><span>1</span><span>2</span><span>›</span></div>
  </main>

  <footer class="site-footer">
    <p class="footer-links">Home | About | Terms | Privacy | Contact</p>
    <p class="footer-note">All models appearing on this site are 18 years or older. Please browse responsibly.<br>Velvet Nook is your secret sanctuary, a friendly team studio based in Sheffield.<br>Flexibility, care and respect for every model, in studio or at home.</p>
    <div class="copyright">© 2024 Velvet Nook. All rights reserved.</div>
    <div class="social"><span></span><span></span><span></span><span></span></div>
  </footer>

  <div class="overlay"></div>

  <div class="age-modal" role="dialog" aria-label="Age verification">
    <div class="age-head">
      <div class="age-big">18+</div>
      <div class="age-sub">Age Verification</div>
    </div>
    <div class="silhouette" role="img" aria-label="Silhouette of a woman in heels with reflection"></div>
    <div class="age-body">
      <p class="age-copy">Please Check the box to enter the site. By Checking the box you agree that<br>you are over 18 years of age or legal age in your state</p>
      <p class="age-title">AGE VERIFICATION</p>
      <div class="age-actions"><span class="age-btn under">UNDER 18</span><span class="age-btn enter">18+ ENTER</span></div>
    </div>
  </div>
</body>
</html>
```